Yoga Workshop - Yoga Practice information flyer

I am a yoga teacher who will be presenting a workshop on yoga for sleep and need a brochure for my clients which outlines a practice that I give them so they can do the practice at home. Ideally I would like a brochure that is a single A3 size of paper in size that folds in half to an A4 booklet with the entire practice on the centre section to make it easy for people to do the practice at home with just one open page in front of them:
* Front page detailing "Yoga for Sleep Workshop" and "Restorative Yoga Practice"
* Centre contains the information on the practice contained in the attached word document. The practice consists of 5 postures, so there needs to be five separate sections which have the pictures of the postures (attached in uploaded files) and the wording contained in the attached word document. All pictures uploaded need to be included in the flyer as each posture has different pictures demonstrating the posture using yoga props or using things people have at home
* Back page containing a picture of myself (picture uploaded in files) with some information about me (contained in the attached word document) and my website www.lumaverisk.com.au

I also need this flyer to be able to printed on 2 double sided A4 sheets of paper so will require 2 x pdf file versions. Importantly, for the centre section of the flyer, the design needs to ensure if it is printed on A4 paper, the wording and pictures for each of the postures are not separated over two pages

Target Market(s)

Existing clients

Requirements
Must have
• Detailed in project description
Nice to have
• The word document also contains some quotes. These do not need to be included in the flyer. If there is room and there is room for one or two of those please include where it would look good
Should not have
• Stock pictures of people in yoga postures which a normal everyday person could not get into

```html
<!DOCTYPE html>
<html lang="en">
<head>
<meta charset="utf-8">
<title>Lumaveri – Yoga for Sleep Brochure</title>
<link href="https://fonts.googleapis.com/css2?family=Bebas+Neue&family=Lora:wght@600&family=Open+Sans:wght@400;600;700&display=swap" rel="stylesheet">
<style>
  :root{
    --navy:#2d3f58;
    --navy-dark:#24344a;
    --copper:#c27f58;
    --copper-light:#d49a76;
    --white:#ffffff;
    --ink:#2a3447;
    --body:#3b4252;
    --canvas:#e8e5e1;
    --mat:#2f8fc4;
    --photo-green:#5d7a3c;
  }
  *{margin:0;padding:0;box-sizing:border-box;}
  html,body{width:1200px;height:1200px;overflow:hidden;}
  body{background:var(--canvas);font-family:"Open Sans",Arial,sans-serif;position:relative;}

  .spread{position:absolute;left:220px;width:760px;height:537px;background:var(--navy);overflow:hidden;box-shadow:0 4px 14px rgba(0,0,0,.18);}
  .spread--outer{top:40px;}
  .spread--inner{top:623px;}
  .fold{position:absolute;left:370px;top:0;width:20px;height:100%;background:linear-gradient(90deg,rgba(0,0,0,0),rgba(0,0,0,.12) 50%,rgba(0,0,0,0));}

  /* Back page */
  .about{position:absolute;left:0;top:0;width:380px;height:100%;color:var(--white);text-align:center;}
  .about__title{position:absolute;top:24px;left:0;width:100%;font-size:13.5px;font-weight:600;color:var(--copper-light);}
  .about__bio{position:absolute;top:56px;left:17px;width:347px;font-size:6.3px;line-height:8.9px;text-align:left;color:#e4e8ee;}
  .quote{position:absolute;left:20px;width:340px;font-size:7.8px;line-height:10.6px;color:#eef1f5;}
  .quote__mark{display:block;margin:0 auto 6px;width:20px;height:15px;}
  .q1{top:126px;} .q2{top:188px;} .q3{top:248px;} .q4{top:325px;}
  .about__web{position:absolute;top:503px;left:0;width:100%;font-size:13.5px;color:var(--white);}

  /* Front cover */
  .cover__paper{position:absolute;left:440px;top:0;width:320px;height:100%;background:var(--white);}
  .cover__photo{position:absolute;left:440px;top:114px;width:320px;height:332px;background:linear-gradient(160deg,#3f6a2c 0%,var(--photo-green) 45%,#8e9a64 75%,#cdbf9a 100%);}
  .cover__curve{position:absolute;left:0;top:0;width:760px;height:537px;}
  .brand{position:absolute;left:510px;top:18px;width:250px;text-align:center;}
  .brand__dot{display:block;margin:0 auto 8px;width:34px;height:34px;border-radius:50%;border:2px solid var(--copper);}
  .brand__name{font-family:"Lora",Georgia,serif;font-weight:600;font-size:19px;color:var(--ink);}
  .brand__tag{margin-top:4px;font-size:6.4px;letter-spacing:1px;color:var(--ink);}
  .cover__title{position:absolute;left:500px;top:460px;width:255px;text-align:center;font-family:"Bebas Neue",Impact,sans-serif;font-size:24.5px;line-height:25px;color:var(--navy);}

  /* Centre spread */
  .practice__oval{position:absolute;left:0;top:0;width:760px;height:537px;}
  .intro{position:absolute;font-size:6.3px;line-height:9px;color:var(--body);}
  .intro--lead{left:198px;top:16px;width:364px;text-align:center;}
  .intro--night{left:155px;top:64px;width:450px;text-align:left;}
  .posture{position:absolute;font-size:6px;line-height:8.6px;color:var(--body);text-align:justify;}
  .posture p{margin-top:5px;}
  .posture strong{font-weight:700;color:var(--ink);}
  .posture__tab{display:inline-block;background:var(--copper);color:var(--white);font-weight:700;font-size:9.5px;line-height:15px;padding:0 12px 0 8px;border-radius:0 8px 8px 0;}
  .posture__name{margin-top:4px;font-size:8.2px;font-weight:700;color:var(--ink);text-align:left;}
  .p1{left:152px;top:102px;width:212px;}
  .p2{left:152px;top:306px;width:212px;}
  .p3{left:397px;top:102px;width:210px;}
  .p4{left:397px;top:276px;width:140px;}
  .p5{left:397px;top:445px;width:200px;}
  .practice__web{position:absolute;left:250px;top:500px;width:114px;text-align:right;font-size:7px;font-weight:600;color:var(--ink);}
  .pose-photo{position:absolute;border-radius:3px;background:linear-gradient(180deg,#3a9bd0,var(--mat) 55%,#2579ab);}
  .ph1{left:21px;top:88px;width:121px;height:190px;}
  .ph2{left:17px;top:306px;width:121px;height:161px;}
  .ph3{left:627px;top:78px;width:118px;height:187px;}
  .ph4{left:547px;top:286px;width:77px;height:117px;background:linear-gradient(180deg,#a2343e,#7d3a4a 55%,#2579ab);}
  .ph5{left:626px;top:334px;width:121px;height:189px;}
</style>
</head>
<body>

<!-- Outer spread: back page + front cover -->
<section class="spread spread--outer" aria-label="Outside of brochure">
  <div class="about">
    <h2 class="about__title">About the teacher...</h2>
    <p class="about__bio">Mara Quillen is a current serving RAN Officer, Yoga Therapist (C-IAYT) and Restful Level 2 instructor. Mara's classes are about using the practices and teaching of Yoga to come to the essence of your true self and learning to tap into the internal wisdom which is always present. Mara is dedicated to making the resilience developing practices of Yoga accessible to all Australian Military personnel and their families.</p>

    <blockquote class="quote q1">
      <svg class="quote__mark" viewBox="0 0 20 15"><path d="M2 14V8Q2 2 8 1M11 14V8Q11 2 17 1M2 8H8V14H2M11 8H17V14H11" fill="none" stroke="var(--copper)" stroke-width="1.2"/></svg>
      “Posture should be steady and comfortable”<br>—Yoga Sutras of Patanjali
    </blockquote>
    <blockquote class="quote q2">
      <svg class="quote__mark" viewBox="0 0 20 15"><path d="M2 14V8Q2 2 8 1M11 14V8Q11 2 17 1M2 8H8V14H2M11 8H17V14H11" fill="none" stroke="var(--copper)" stroke-width="1.2"/></svg>
      “Tension is who you think you are, Relaxation is who you actually are”
    </blockquote>
    <blockquote class="quote q3">
      <svg class="quote__mark" viewBox="0 0 20 15"><path d="M2 14V8Q2 2 8 1M11 14V8Q11 2 17 1M2 8H8V14H2M11 8H17V14H11" fill="none" stroke="var(--copper)" stroke-width="1.2"/></svg>
      “Life isn’t as serious as the mind makes it out to be”<br>—Orin Vale
    </blockquote>
    <blockquote class="quote q4">
      <svg class="quote__mark" viewBox="0 0 20 15"><path d="M2 14V8Q2 2 8 1M11 14V8Q11 2 17 1M2 8H8V14H2M11 8H17V14H11" fill="none" stroke="var(--copper)" stroke-width="1.2"/></svg>
      “Watch your thoughts, they become words<br>Watch your words, they become actions<br>Watch your actions, they become habits<br>Watch your habits, they become character<br>Watch your character, for it becomes your destiny”<br>—Upanishads
    </blockquote>
    <p class="about__web">www.lumaverisk.com.au</p>
  </div>

  <div class="cover__paper"></div>
  <div class="cover__photo" role="img" aria-label="Photo of the teacher sitting cross-legged in meditation on a blanket in a grassy park"></div>
  <svg class="cover__curve" viewBox="0 0 760 537" aria-hidden="true">
    <path d="M440 0H492Q430 270 500 537H440Z" fill="var(--navy)"/>
    <path d="M492 0Q430 270 500 537" fill="none" stroke="var(--copper)" stroke-width="5"/>
  </svg>
  <div class="brand">
    <span class="brand__dot"></span>
    <div class="brand__name">Lumaveri</div>
    <div class="brand__tag">Be the change you wish to see in the world</div>
  </div>
  <h1 class="cover__title">Yoga for Sleep Workshop &amp;<br>Restorative Yoga Practice</h1>
  <div class="fold"></div>
</section>

<!-- Inner spread: the practice -->
<section class="spread spread--inner" aria-label="Restorative practice">
  <svg class="practice__oval" viewBox="0 0 760 537" aria-hidden="true">
    <ellipse cx="380" cy="268" rx="326" ry="336" fill="none" stroke="var(--copper)" stroke-width="4"/>
    <ellipse cx="380" cy="268" rx="320" ry="330" fill="var(--white)"/>
  </svg>
  <div class="fold"></div>

  <p class="intro intro--lead">Use this sequence to relax and unwind at the end of a day or before bed. Settle comfortably into each posture for about 5-7 minutes. Set a timer to let you know when it is time to change position, and you can also listen to any music you find relaxing at the same time. The audio recording from the Yoga for Sleep Workshop can also be used to recreate the practice at home.</p>
  <p class="intro intro--night">In the middle of the night when you can’t sleep, you might like to try getting up and resting in any one of these postures for about 5-10 minutes before heading back to bed.</p>

  <article class="posture p1">
    <span class="posture__tab">POSTURE 1 –</span>
    <h3 class="posture__name">Supported Chest Opening with Knee Support</h3>
    <p><strong>PROPS –</strong> 2 x bolsters (or towels rolled up lengthways), 1 x cushion for head support (optional)</p>
    <p><strong>SET UP NOTES –</strong> Position the props in a T-position with one bolster/towel running parallel to the yoga mat and one bolster towel running horizontal to the mat underneath the knees. Position yourself so your buttocks is on the floor and the parallel bolster runs from the lower back up to behind the head.</p>
    <p><strong>CAUTION –</strong> If any lower back pain is experience adjust the parallel bolster height by using a towel. If using a towel, the height of the parallel support prop can be adjusted by either using a thinner towel or loosely rolling the towel. Do not us any parallel support prop if pain continues.</p>
  </article>

  <article class="posture p2">
    <span class="posture__tab">POSTURE 2 –</span>
    <h3 class="posture__name">Supported Bound-Angle Pose</h3>
    <p><strong>PROPS –</strong> 1 x bolsters (or towel rolled up lengthways), 2 x yoga blocks/bolsters (or pillows), 1 x cushion for head support (optional)</p>
    <p><strong>SET UP NOTES –</strong> Similar to Posture 1 without the bolster behind the knees. Instead, the soles of the feet are together with knees wide being supported by either blocks, bolsters or pillows.</p>
    <p><strong>CAUTION –</strong> If any lower back pain is experience adjust the parallel bolster height by using a towel. If using a towel, the height of the parallel support prop can be adjusted by either using a thinner towel or loosely rolling the towel. Do not us any parallel support prop if pain continues.</p>
  </article>

  <article class="posture p3">
    <span class="posture__tab">POSTURE 3 –</span>
    <h3 class="posture__name">Elevated Legs-Up-the-Wall Pose</h3>
    <p><strong>PROPS –</strong> 1 x bolsters (or towel or blanket densely folded to a width of about 15-30cm), 1 x cushion for head support (optional)</p>
    <p><strong>SET UP NOTES –</strong> To enter the posture sit at 90 degrees to the wall with the side of your hip about a hand width away from the wall, and the bolster/folded towel or blanket close by. Lie down on the mat on your side then roll onto your back and extend feet up wall. The feet can push into the wall to elevate the hips slightly so the bolster/folded towel or blanket can slide underneath the hips. The prop should be positioned underneath the sacrum (flat bony structure at the base of the spine).</p>
    <p><strong>CAUTION –</strong> If any lower back pain is experience adjust the height the hips are elevated by using a towel or blanket that is folded to a lower height.</p>
  </article>

  <article class="posture p4">
    <span class="posture__tab">POSTURE 4 –</span>
    <h3 class="posture__name">Posture 4 – Supported Child’s Pose</h3>
    <p><strong>Props –</strong> 1-2 x bolsters (or 3-4 bed pillows)</p>
    <p><strong>Set up notes –</strong> Position bolster or stacked pillows under torso. Rest the head in one direction and remember to turn to the head to the other side half way through the time you spend in this posture.</p>
    <p><strong>Caution –</strong> If any knee or hip pain is experience, increase the height of the support under the torso by adding more bolsters, folded blankets or pillows.</p>
  </article>

  <article class="posture p5">
    <span class="posture__tab">POSTURE 5 –</span>
    <h3 class="posture__name">Basic Relaxation Posture with Knee Support</h3>
    <p><strong>Props –</strong> 1x bolsters (or 1 x bed pillows or rolled up towel)</p>
    <p><strong>Set up notes –</strong> Reclining on back, position bolster<br>or pillows under knees.</p>
  </article>

  <p class="practice__web">www.lumaverisk.com.au</p>

  <div class="pose-photo ph1" role="img" aria-label="Photo: woman reclining on a blue mat over a lengthways bolster with a bolster under the knees"></div>
  <div class="pose-photo ph2" role="img" aria-label="Photo: woman in supported bound-angle pose with knees resting on blocks"></div>
  <div class="pose-photo ph3" role="img" aria-label="Photo: woman lying with hips on a bolster and legs raised up the wall"></div>
  <div class="pose-photo ph4" role="img" aria-label="Photo: woman in child's pose resting her torso on a bolster"></div>
  <div class="pose-photo ph5" role="img" aria-label="Photo: woman lying on her back with pillows under the knees"></div>
</section>

</body>
</html>
```